Extremely Professional Lawyer needs letterhead for new boutique real estate law firm

I need letterhead for my new solo practice law firm. I practiced as a partner in a huge global law firm for years. Now I am starting a solo firm where I will deliver very high-quality legal services that are real-estate focused. The idea is that my practice will be very focused but that the services will be at the quality level provided by partners at high-profile law firms. The name of my law firm will be Brenner Law Group, LLC. For now, I am the only lawyer. I expect to negotiate and draft house sale/purchase contracts and close house deals. Eventually, I would like to do small-scale development deals for developer clients, a specialty of mine.

Industry/Entity Type

Boutique

```html
<!DOCTYPE html>
<html lang="en">
<head>
<meta charset="utf-8">
<title>Brenner Law Group, LLC — Letterhead</title>
<link href="https://fonts.googleapis.com/css2?family=Aleo:wght@400;700&display=swap" rel="stylesheet">
<style>
  :root {
    --backdrop: #e9ecf1;
    --paper: #ffffff;
    --brand-blue: #0d3f86;
    --brand-grey: #9a9ea6;
    --footer-text: #dfe7f4;
  }
  html, body {
    margin: 0;
    padding: 0;
    width: 900px;
    height: 1200px;
    overflow: hidden;
    background: var(--backdrop);
    font-family: "Aleo", Georgia, serif;
  }
  .letterhead {
    position: absolute;
    left: 70px;
    top: 80px;
    width: 760px;
    height: 1040px;
    background: var(--paper);
    box-shadow: 0 6px 24px rgba(13, 63, 134, 0.18);
    overflow: hidden;
  }
  .firm-mark {
    position: absolute;
    top: 58px;
    left: 0;
    right: 0;
    display: flex;
    flex-direction: column;
    align-items: center;
    gap: 10px;
  }
  .firm-mark__square {
    width: 22px;
    height: 22px;
    background: var(--brand-blue);
  }
  .firm-mark__name {
    font-size: 26px;
    font-weight: 700;
    color: var(--brand-blue);
    letter-spacing: 0.2px;
    margin: 0;
  }
  .footer-rule {
    position: absolute;
    left: 0;
    right: 0;
    bottom: 88px;
    height: 8px;
    background: var(--brand-grey);
  }
  .footer-band {
    position: absolute;
    left: 0;
    right: 0;
    bottom: 0;
    height: 88px;
    background: var(--brand-blue);
    display: flex;
    gap: 68px;
    padding: 14px 0 0 18px;
    box-sizing: border-box;
    color: var(--footer-text);
    font-size: 11.5px;
    line-height: 1.38;
  }
  .footer-band p { margin: 0; white-space: nowrap; }
  .contact-column--phone .spacer { height: 8px; }
</style>
</head>
<body>
  <main class="letterhead">
    <header class="firm-mark">
      <div class="firm-mark__square"></div>
      <h1 class="firm-mark__name">Brenner Law Group, LLC</h1>
    </header>

    <div class="footer-rule"></div>
    <footer class="footer-band">
      <div class="contact-column contact-column--address">
        <p>Adress : Street UNIT 3140 BOX 725</p>
        <p>city Larkmont</p>
        <p>state WESTHAVEN PROVINCE</p>
        <p>zip code 00417 - 2308</p>
      </div>
      <div class="contact-column contact-column--phone">
        <p>Phone : xxx-xxx-xxx</p>
        <div class="spacer"></div>
        <p>email : office@brennerlaw.example</p>
        <p>www.brennerlaw.example</p>
      </div>
    </footer>
  </main>
</body>
</html>
```